Serene Spiritual Website Wanted for World Wide Organisation

We need a serene, clean web design for our organisation that works around the world.

What We Do
We aim to bring life into synergy across the world. We inspire, motivate, synchronise, and harmonise. We work with energy which is essential to all of life (environmental, human & animal). Our website must depict the spiritual element of being innately natural and reflect animism.

We have included a PDF attachment with details of the structure, navigation, and some websites for ideas/reference. The logo is also attached.
Updates

Target Market(s)

Anyone over 18yrs looking for answers to life's big questions or looking to develop themselves

Industry/Entity Type

Spiritual/wellbeing/Self Development

Number of Pages Required

5+ page

Requirements
Must have
• It must be serene and natural looking, it must incorporate the logo.
Nice to have
• We have included a Powerpoint document which may help you understand what we need, it is just an idea for structure and style, it is not set in stone so feel free to be as creative as you like!
Should not have
• Not clinical.

```html
<!DOCTYPE html>
<html lang="en">
<head>
<meta charset="utf-8">
<title>Harmonara</title>
<link href="https://fonts.googleapis.com/css2?family=Poppins:wght@300;400;500;600;700&display=swap" rel="stylesheet">
<style>
:root{
  --purple:#3b3466;
  --purple-deep:#2e2854;
  --gold:#d8c77c;
  --gold-text:#c9b25a;
  --ink:#3b3466;
  --body:#6d6a7c;
  --white:#ffffff;
  --mist:#f4f1f6;
}
*{margin:0;padding:0;box-sizing:border-box}
html,body{width:1200px;height:4036px;overflow:hidden;background:var(--white)}
body{font-family:'Poppins',sans-serif;color:var(--ink)}
.page{position:relative;width:1200px;height:4036px;overflow:hidden}
.abs{position:absolute}
.btn{position:absolute;display:flex;align-items:center;justify-content:center;border-radius:40px;font-size:17px;font-weight:500}
.btn-dark{background:var(--purple);color:var(--white)}
.btn-gold{background:var(--gold);color:var(--white)}
.para{font-size:15px;line-height:27px;color:var(--body)}
.photo{position:absolute}

/* header */
.contact-bar{left:600px;top:0;width:600px;height:46px;background:var(--purple);color:var(--white);font-size:15px;display:flex;align-items:center;padding-left:52px;gap:18px}
.nav{top:64px;left:0;width:1200px;height:40px}
.nav a{position:absolute;font-size:15px;font-weight:500;color:var(--ink);text-decoration:none;letter-spacing:.5px}
.brand-badge{left:112px;top:0;width:188px;height:188px;border-radius:50%;background:var(--purple);border:6px solid #d7d1e6;display:flex;align-items:center;justify-content:center;z-index:5}
.brand-badge span{color:var(--gold);font-size:24px;font-weight:600}

/* hero */
.hero-photo{left:0;top:120px;width:1200px;height:680px;background:linear-gradient(180deg,#0a78b0 0%,#2aa5d3 45%,#58c3e3 75%,#8ad7ea 100%)}
.hero-title{top:290px;width:1200px;text-align:center;font-size:76px;font-weight:600;color:var(--white)}
.hero-sub{top:400px;width:1200px;text-align:center;font-size:22px;line-height:44px;font-weight:600;color:var(--white)}
.dots{top:716px;left:560px;display:flex;gap:12px}
.dots i{width:14px;height:14px;border-radius:50%;border:2px solid var(--white);display:block}
.dots i.on{background:var(--white)}

/* section titles */
.section-title{font-size:38px;font-weight:600;color:var(--ink);letter-spacing:1px}
.mark{width:46px;height:46px;border-radius:50%;background:var(--purple)}

/* synergy cards */
.card{position:absolute;top:1620px;width:476px;height:580px;background:var(--white);border-radius:26px;box-shadow:0 10px 30px rgba(59,52,102,.18);overflow:hidden;text-align:center}
.card .photo{left:0;top:0;width:476px;height:320px}
.card h3{position:absolute;top:330px;width:100%;font-size:34px;font-weight:500}
.card .para{position:absolute;top:384px;left:44px;width:388px;font-size:14px;line-height:24px}
.card .btn{left:158px;top:508px;width:160px;height:52px;font-size:15px}

/* footer */
.footer{left:0;top:3560px;width:1200px;height:476px;background:var(--purple)}
.footer-nav a{position:absolute;top:3850px;font-size:15px;color:var(--white);text-decoration:none;letter-spacing:.5px}
.socials{top:3908px;left:500px;display:flex;gap:14px}
.socials i{display:block;width:30px;height:30px;border-radius:50%;border:2px solid var(--white)}
</style>
</head>
<body>
<div class="page">

  <!-- header -->
  <div class="abs contact-bar"><span>Call us: +1 555 010 0199</span><span>|</span><span>Email: hello@harmonara.example</span></div>
  <nav class="abs nav">
    <a style="left:640px">EVENTS</a>
    <a style="left:760px">ABOUT</a>
    <a style="left:868px">SYNERGISE</a>
    <a style="left:1000px">WISDOM</a>
    <a style="left:1098px">SHOP</a>
  </nav>
  <div class="abs brand-badge"><span>Harmonara</span></div>

  <!-- hero -->
  <div class="photo hero-photo" role="img" aria-label="Sunlit clear blue water surface with light ripples"></div>
  <h1 class="abs hero-title">Harmonara</h1>
  <p class="abs hero-sub">Sed ut perspiciatis unde omnis iste natus error sit volup<br>totem accusantium doloremque laudantium</p>
  <div class="btn btn-dark" style="left:528px;top:504px;width:144px;height:50px;font-size:15px">READ MORE</div>
  <div class="abs dots"><i class="on"></i><i></i><i></i></div>
  <svg class="abs" style="left:0;top:640px" width="1200" height="180" viewBox="0 0 1200 180">
    <path d="M0 90 C250 190 500 170 720 100 C900 40 1060 30 1200 70 L1200 180 L0 180 Z" fill="#ffffff"/>
    <path d="M0 95 C250 190 500 170 720 105 C900 48 1060 40 1200 80" fill="none" stroke="var(--purple)" stroke-width="22"/>
    <path d="M0 120 C260 200 520 175 740 118 C920 70 1070 62 1200 95" fill="none" stroke="var(--gold)" stroke-width="3"/>
  </svg>

  <!-- about -->
  <div class="abs" style="left:128px;top:850px;width:484px;height:484px;border-radius:50%;background:#b9b3cc"></div>
  <div class="photo" style="left:150px;top:872px;width:440px;height:440px;border-radius:50%;background:radial-gradient(circle at 50% 35%,#f3d58a 0%,#d89b4a 35%,#8d6a52 65%,#4a3f46 100%)" role="img" aria-label="Person meditating on a rock above the clouds at sunrise"></div>
  <h2 class="abs section-title" style="left:648px;top:922px">SAY HARMONARA</h2>
  <p class="abs para" style="left:648px;top:982px;width:470px;font-size:14px;line-height:25px">Sed ut perspiciatis unde omnis iste natus error sit voluptatem accusantium doloremque laudantium, totam rem aperiam, eaque ipsa quae ab illo inventore veritatis et quasi architecto beatae vitae dicta sunt explicabo. Nemo enim ipsam voluptatem quia voluptas sit aspernatur aut odit aut fugit, sed quia consequuntur magni dolores eos qui ratione voluptatem sequi nesciunt. Neque porro quisquam est, qui dolorem ipsum quia dolor sit amet, consectetur, adipisci velit, sed quia non numquam eius modi tempora incidunt ut labore et dolore magnam aliquam quaerat voluptatem.</p>
  <div class="btn btn-dark" style="left:648px;top:1246px;width:160px;height:54px">Read More &#8594;</div>

  <!-- synergy -->
  <div class="photo" style="left:0;top:1440px;width:1200px;height:900px;background:radial-gradient(ellipse at 50% 50%,#ffffff 0%,#f6f2ea 55%,#ece4d6 100%)" role="img" aria-label="Soft faded background of a calm meditation space"></div>
  <svg class="abs" style="left:0;top:1420px" width="1200" height="120" viewBox="0 0 1200 120">
    <path d="M0 0 L1200 0 L1200 110 C900 20 300 20 0 110 Z" fill="#ffffff"/>
    <path d="M0 110 C300 20 900 20 1200 110" fill="none" stroke="var(--purple)" stroke-width="6"/>
    <path d="M0 96 C300 8 900 8 1200 96" fill="none" stroke="var(--gold)" stroke-width="2"/>
  </svg>
  <div class="abs mark" style="left:577px;top:1466px"></div>
  <h2 class="abs section-title" style="left:0;width:1200px;text-align:center;top:1516px">SYNERGY</h2>

  <div class="card" style="left:112px">
    <div class="photo" style="background:linear-gradient(160deg,#b8a58a,#6e5a48 60%,#3c3330)" role="img" aria-label="Woman sitting cross-legged with a singing bowl in a bright room"></div>
    <h3>Pathways</h3>
    <p class="para">Sed ut perspiciatis unde omnis iste natus error sit voluptatem accusantium doloremque laudantium, totam rem aperiam, eaque ipsa quae ab illo inventore veritatis et quasi architecto beatae vitae dicta sunt explicabo.</p>
    <div class="btn btn-gold">Learn More</div>
  </div>
  <div class="card" style="left:616px">
    <div class="photo" style="background:linear-gradient(160deg,#4e88b4,#b08a4c 55%,#6d5a3a)" role="img" aria-label="Person lying relaxed among brass singing bowls"></div>
    <h3>Energies</h3>
    <p class="para">Sed ut perspiciatis unde omnis iste natus error sit voluptatem accusantium doloremque laudantium, totam rem aperiam, eaque ipsa quae ab illo inventore veritatis et quasi architecto beatae vitae dicta sunt explicabo.</p>
    <div class="btn btn-gold">Learn More</div>
  </div>

  <svg class="abs" style="left:0;top:2240px" width="1200" height="120" viewBox="0 0 1200 120">
    <path d="M0 0 C300 100 900 100 1200 0 L1200 120 L0 120 Z" fill="#ffffff"/>
    <path d="M0 0 C300 100 900 100 1200 0" fill="none" stroke="var(--purple)" stroke-width="6"/>
    <path d="M0 14 C300 112 900 112 1200 14" fill="none" stroke="var(--gold)" stroke-width="2"/>
  </svg>

  <!-- events -->
  <div class="abs mark" style="left:577px;top:2390px"></div>
  <h2 class="abs section-title" style="left:0;width:1200px;text-align:center;top:2438px">SYNCHRONISE</h2>
  <div class="photo" style="left:132px;top:2540px;width:448px;height:360px;border-radius:18px;background:linear-gradient(150deg,#d9b48a,#9b6b3f 50%,#4b3426)" role="img" aria-label="Hands playing a brass singing bowl beside a row of bowls"></div>
  <h3 class="abs" style="left:632px;top:2556px;width:520px;font-size:26px;line-height:38px;font-weight:500">SED UT PERSPICIATIS UNDE OMNIS ISTE NATUS ERROR SIT VOLUPTATEM</h3>
  <p class="abs" style="left:632px;top:2672px;font-size:19px;font-weight:500;color:var(--gold-text)">22 AUGUST 2022</p>
  <p class="abs para" style="left:632px;top:2714px;width:480px;font-size:14px;line-height:24px">Nemo enim ipsam voluptatem quia voluptas sit aspernatur aut odit aut fugit, sed quia consequuntur magni dolores eos qui ratione voluptatem sequi nesciunt. Neque porro quisquam est, qui dolorem ipsum quia dolor sit amet, consectetur, adipisci velit.</p>
  <p class="abs" style="left:632px;top:2860px;font-size:17px;font-weight:500">Book My Space &#8594;</p>
  <div class="btn btn-gold" style="left:516px;top:2956px;width:168px;height:52px;font-size:16px">More Events</div>

  <!-- synchrony -->
  <div class="photo" style="left:0;top:3060px;width:1200px;height:560px;background:linear-gradient(180deg,#6a7c98 0%,#c99a6a 40%,#f1b25a 60%,#7d4a2c 100%)" role="img" aria-label="Man meditating on a cliff edge at sunset with birds in flight"></div>
  <h2 class="abs section-title" style="left:604px;top:3166px;color:var(--white)">SYNCHRONY</h2>
  <p class="abs para" style="left:604px;top:3222px;width:440px;font-size:14px;line-height:24px;color:var(--white)">Sed ut perspiciatis unde omnis iste natus error sit voluptatem accusantium doloremque laudantium, totam rem aperiam, eaque ipsa quae ab illo inventore veritatis et quasi architecto beatae vitae dicta sunt explicabo. Nemo enim ipsam voluptatem quia voluptas sit aspernatur.</p>
  <div class="btn btn-dark" style="left:604px;top:3394px;width:160px;height:54px">Read More</div>

  <!-- footer -->
  <div class="abs footer"></div>
  <svg class="abs" style="left:0;top:3520px" width="1200" height="200" viewBox="0 0 1200 200">
    <path d="M0 120 C250 40 450 30 700 90 C900 140 1060 120 1200 60 L1200 200 L0 200 Z" fill="var(--purple)"/>
    <path d="M0 140 C250 70 450 60 700 120 C900 168 1060 150 1200 96" fill="none" stroke="var(--gold)" stroke-width="14"/>
    <path d="M0 162 C250 96 450 86 700 144 C900 190 1060 174 1200 122" fill="none" stroke="#ffffff" stroke-width="3"/>
  </svg>
  <p class="abs" style="left:0;width:1200px;top:3748px;text-align:center;font-size:40px;font-weight:600;color:var(--gold)">Harmonara</p>
  <div class="footer-nav">
    <a style="left:326px">EVENTS</a>
    <a style="left:448px">ABOUT</a>
    <a style="left:562px">SYNERGISE</a>
    <a style="left:704px">WISDOM</a>
    <a style="left:832px">SHOP</a>
  </div>
  <div class="abs socials"><i></i><i></i><i></i><i></i><i></i><i></i></div>
  <p class="abs" style="left:0;width:1200px;top:3966px;text-align:center;font-size:15px;color:var(--white)">&copy; Copyright 2022 <span style="color:var(--gold)">Harmonara</span>.All Rights Reserved</p>

</div>
</body>
</html>
```